依頼詳細
PCとスマホデザインの両方納品をいただきますが、
まずはデザインイメージが確認しやすいPCページのみの提案をお願いします。
スマホページは当選者に納品時にお願いしたいと思います。
スマホサイズについて、カンバスサイズは横幅375pxで作成し、2倍の横幅750pxのサイズで書き出ししてください。
(Retinaディスプレイに対応するため)
スマホページ作成時は、メニューが展開した際のデザインもお願いします。
レスポンシブウェブデザインを意識したデザインでお願いします。

■サイトマップ
添付の画面遷移図をご確認ください。

■参考サイト
https://www.hirotoku-sarumi.jp/
https://www.tabuse-seiban.co.jp/

■内容について
主に鋼材の卸売業を行う会社の公式サイトになります。
卸売だけでなく、鋼板を仕入れて希望のサイズに切断、プレスなどの加工も行う会社です。
参考サイトはメインビジュアルが動画になっていますが、今回のサイトデザインでは動画を使用する予定は今のところありません。

■素材写真
画像データについては、フリー素材から流用して
イメージ画像に当て込んでください。
足りない場合は、一旦他のサイトの写真をサンプルとして
入れてください。(サンプルなどの表記をお願いします)
また、購入が必要な写真などを利用した場合、
価格とサイト名を教えてください。

また、Pixoral Imageで定期契約をしていますので、
Pixoral Imageの画像は使用できます。
デザイン時はカンプ画像をお入れいただきますようお願いします。

■ロゴについて
添付のロゴデータを使用してください。

■ワイヤーフレーム
https://mock.velqara.net/view/52817caa-1f3b-4d0e-9a72-6e1b8c37d904-b39f/?fullscreen
コンテンツの構成としてワイヤーフレームを作成しましたが
必ずしもワイヤーフレームの通りではなくて大丈夫です。
TOPページに配置するコンテンツを見ていただき、デザインは
デザイナーの皆様におまかせしたいと思います。

----------------------------------------------------------------------------
【制作物に対するお願い】

■フォントについて
・無料で使えるフォントで作成をお願いします。
・OSに紐づくフォントの使用は控えていただければと思います (ヒラギノなど)

ページ数
1ページ
希望イメージ
シンプル 複雑
単色 カラフル
暗い 明るい
日常 高級
遊び心 厳粛
未来的 伝統的
女性的 男性的
希望する色
ベースカラー:白、青、ポイントカラー:赤
納品ファイル
• 高解像度JPG (.jpg)
• イラストレーター形式 (.ai)
• フォトショップ形式 (.psd)
補足説明
上記のいずれか1つ(アウトラインありとなしの2つ)と高解像度JPGを納品お願いします。
adobe XDでの納品も可能です。
CS5にバージョンを落としたロゴデータです。
ロゴのpngデータも追加しました。

```html
<!DOCTYPE html>
<html lang="ja">
<head>
<meta charset="utf-8">
<title>越前カナメ鋼業株式会社</title>
<link href="https://fonts.googleapis.com/css2?family=Noto+Sans+JP:wght@400;500;700&family=Montserrat:wght@400;500;600&display=swap" rel="stylesheet">
<style>
:root{
  --red:#d9141b;
  --ink:#1a1a1a;
  --grey:#6b6b6b;
  --line:#d8d8d8;
  --paper:#ffffff;
  --dark:#1c1c1e;
}
*{margin:0;padding:0;box-sizing:border-box}
html,body{width:1200px;height:4100px;overflow:hidden}
body{position:relative;background:var(--paper);color:var(--ink);font-family:"Noto Sans JP",sans-serif}
.abs{position:absolute}
.en{font-family:"Montserrat",sans-serif}
.photo{position:absolute}
.brand{display:flex;align-items:center;gap:12px;font-weight:700;font-size:22px;color:var(--red)}
.brand .mark{width:18px;height:18px;background:var(--red)}
/* header */
.site-header{left:0;top:0;width:1200px;height:120px}
.site-header .brand{position:absolute;left:40px;top:42px}
.global-nav{position:absolute;left:532px;top:52px;display:flex;gap:32px;font-size:15px;font-weight:500}
.header-tel{position:absolute;left:800px;top:24px;text-align:left}
.header-tel small{display:block;font-size:11px;color:var(--grey)}
.header-tel strong{display:block;font-family:"Montserrat",sans-serif;font-size:30px;font-weight:600;letter-spacing:1px;line-height:1.2}
.header-contact{position:absolute;left:1080px;top:0;width:120px;height:120px;background:var(--red);color:#fff;font-size:13px;display:flex;flex-direction:column;align-items:center;justify-content:center;gap:8px}
/* hero */
.hero-title{left:64px;top:236px;font-size:66px;font-weight:700;line-height:1.3;letter-spacing:2px}
.hero-lead{left:64px;top:432px;font-size:42px;font-weight:500;line-height:1.4}
.hero-note{left:64px;top:580px;font-size:14px;color:var(--grey);line-height:1.8;width:400px}
.hero-photo{left:532px;top:132px;width:668px;height:600px;border-radius:0 0 0 80px;background:radial-gradient(circle at 45% 55%,#f3a54a 0,#b36a2a 12%,#4b4d55 40%,#22252b 100%)}
/* labels & buttons */
.label{font-family:"Montserrat",sans-serif;font-size:15px;color:var(--red);font-weight:500}
.btn-dark{background:var(--ink);color:#fff;font-size:14px;display:flex;align-items:center;justify-content:center}
.btn-line{border:1px solid currentColor;font-size:14px;display:flex;align-items:center;justify-content:center}
/* about */
.about-label{left:64px;top:786px}
.about-title{left:64px;top:836px;font-size:54px;font-weight:700;line-height:1.35}
.about-text{left:532px;top:960px;width:620px;font-size:15px;line-height:2;color:#333}
.about-btn{left:532px;top:1180px;width:200px;height:52px}
/* dark products band */
.products-band{left:0;top:1820px;width:1128px;height:540px;border-radius:0 60px 60px 0;background:linear-gradient(120deg,#3a3e45 0%,#23262b 55%,#151619 100%)}
.products-title{left:64px;top:1900px;font-size:58px;font-weight:700;color:#fff;line-height:1.4}
.products-text{left:64px;top:2080px;width:520px;font-size:14px;line-height:1.9;color:#ddd}
.products-btn{left:64px;top:2200px;width:200px;height:52px;color:#fff}
.band-link{color:#fff;font-size:14px;display:flex;align-items:center;gap:14px}
.circle-arrow{width:48px;height:48px;border:1px solid #fff;border-radius:50%;display:flex;align-items:center;justify-content:center}
/* product cards */
.card{top:2480px;width:330px;height:150px;display:flex;gap:20px}
.card .thumb{width:140px;height:140px;flex:none}
.card .body{flex:1;min-width:0}
.card h3{font-size:26px;font-weight:500;margin-top:14px;color:var(--ink)}
.card p{font-size:12px;color:var(--grey);line-height:1.8;margin-top:10px}
.slider-btn{top:2650px;width:64px;height:34px;border:1px solid var(--line);border-radius:17px;display:flex;align-items:center;justify-content:center}
/* recruit */
.recruit-photo{left:72px;top:2752px;width:396px;height:600px;background:linear-gradient(160deg,#8fa3b8 0%,#5b6e82 45%,#3a4653 100%)}
.recruit-panel{left:468px;top:2752px;width:732px;height:600px;background:var(--red);color:#fff;padding:72px 80px}
.recruit-panel .label{color:#fff}
.recruit-panel h2{font-size:56px;font-weight:500;line-height:1.35;margin-top:18px}
.recruit-panel p{font-size:14px;line-height:1.9;margin-top:26px;width:540px}
.recruit-panel .btn-line{width:200px;height:52px;margin-top:34px}
/* information */
.info{left:72px;top:3428px;display:flex;align-items:center;gap:40px;width:1060px;padding-bottom:24px;border-bottom:1px solid var(--line)}
.info h2{font-size:30px;font-weight:500}
.info p{font-size:14px;color:#333}
/* footer */
.site-footer{left:0;top:3572px;width:1200px;height:528px;background:var(--dark);color:#fff}
.footer-note{position:absolute;left:0;width:1200px;top:36px;text-align:center;font-size:13px;color:#bbb}
.footer-contact{position:absolute;top:84px;display:flex;flex-direction:column;align-items:center;width:600px}
.footer-contact .big{display:flex;align-items:center;gap:14px;font-size:40px;font-family:"Montserrat",sans-serif;font-weight:500}
.footer-contact small{font-size:12px;color:#aaa;margin-top:6px}
.footer-divider{position:absolute;left:600px;top:84px;width:1px;height:110px;background:#555}
.site-footer .brand{position:absolute;left:64px;top:300px;color:#fff}
.footer-nav{position:absolute;left:64px;top:352px;display:flex;gap:28px;font-size:14px}
.footer-address{position:absolute;left:64px;top:396px;font-size:12px;color:#bbb}
.footer-bottom{position:absolute;left:64px;top:430px;font-size:11px;color:#999;display:flex;gap:28px}
.to-top{position:absolute;left:1088px;top:420px;width:52px;height:52px;border:1px solid #777;border-radius:50%;display:flex;align-items:center;justify-content:center}
</style>
</head>
<body>

<header class="abs site-header">
  <div class="brand"><span class="mark"></span>越前カナメ鋼業株式会社</div>
  <nav class="global-nav"><span>事業内容</span><span>会社概要</span><span>採用情報</span></nav>
  <div class="header-tel"><small>ご質問やご相談はお気軽にどうぞ</small><strong>0256-41-7730</strong><small>受付時間 8:00〜17:00(土日祝除く)</small></div>
  <div class="header-contact">
    <svg width="26" height="20" viewBox="0 0 26 20"><rect x="1" y="1" width="24" height="18" fill="none" stroke="#fff" stroke-width="2"/><path d="M1 1l12 10 12-10" fill="none" stroke="#fff" stroke-width="2"/></svg>
    お問い合わせ
  </div>
</header>

<h1 class="abs hero-title">鋼材・鋼板の<br>卸売と加工</h1>
<p class="abs hero-lead">お客様のニーズに<br>お応えします</p>
<p class="abs hero-note">シャーリングによる切断やプレス、ベンダーによる曲げ加工などができる鋼材問屋です。</p>
<div class="photo hero-photo" role="img" aria-label="火花を散らしながら鋼材をグラインダーで切断する作業の写真"></div>

<span class="abs label about-label">About</span>
<h2 class="abs about-title">越前カナメ<br>鋼業について</h2>
<p class="abs about-text">当社は新潟県燕市で創業以来、鋼材・鋼板の卸売を通じて地域の製造業を支えてまいりました。仕入れた鋼板をご希望のサイズに切断し、プレスや曲げ加工まで一貫して対応いたします。豊富な在庫と確かな技術で、お客様の多様なご要望に迅速にお応えします。</p>
<div class="abs btn-dark about-btn">事業内容</div>

<div class="photo" style="left:0;top:1160px;width:220px;height:220px;background:linear-gradient(150deg,#c9b48a,#6e6552 60%,#3e3a33)" role="img" aria-label="鋼材が並ぶ倉庫内の写真"></div>
<div class="photo" style="left:928px;top:1280px;width:120px;height:160px;background:linear-gradient(160deg,#9aa7b5,#4c5866)" role="img" aria-label="作業服姿のスタッフが作業する写真"></div>
<div class="photo" style="left:1080px;top:1260px;width:120px;height:180px;background:linear-gradient(160deg,#b8b2a4,#5e5a52)" role="img" aria-label="工場内の加工機械の写真"></div>
<div class="photo" style="left:468px;top:1412px;width:400px;height:308px;background:linear-gradient(140deg,#a89e8a,#5b554a 55%,#2f2c27)" role="img" aria-label="鋼材倉庫で作業するスタッフの写真"></div>

<div class="abs products-band" role="img" aria-label="積み上げられた鋼材の写真"></div>
<h2 class="abs products-title">多種多様な製品群と<br>鋼材加工でお応え</h2>
<p class="abs products-text">棒鋼・鋼管・鋼板をはじめ幅広い鋼種を取り揃え、切断から加工までご要望に合わせて柔軟に対応いたします。小ロットのご注文もお気軽にご相談ください。</p>
<div class="abs btn-line products-btn">事業内容</div>
<div class="abs band-link" style="left:700px;top:2282px">取り扱い鋼種<span class="circle-arrow"><svg width="16" height="10" viewBox="0 0 16 10"><path d="M0 5h14M10 1l4 4-4 4" stroke="#fff" fill="none"/></svg></span></div>
<div class="abs band-link" style="left:900px;top:2282px">取り扱い製品<span class="circle-arrow"><svg width="16" height="10" viewBox="0 0 16 10"><path d="M0 5h14M10 1l4 4-4 4" stroke="#fff" fill="none"/></svg></span></div>

<div class="abs card" style="left:128px"><div class="thumb" role="img" aria-label="棒鋼の断面の写真" style="background:linear-gradient(135deg,#9097a0,#3d4148)"></div><div class="body"><h3>棒鋼</h3><p>丸鋼、角鋼、平鋼など各種規格を在庫しています。</p></div></div>
<div class="abs card" style="left:500px"><div class="thumb" role="img" aria-label="鋼管の写真" style="background:linear-gradient(135deg,#b9bec4,#5a5f66)"></div><div class="body"><h3>鋼管</h3><p>丸パイプ、角パイプ、配管用鋼管などを取り扱います。</p></div></div>
<div class="abs card" style="left:870px"><div class="thumb" role="img" aria-label="鋼板の写真" style="background:linear-gradient(135deg,#8a8f96,#2f3238)"></div><div class="body"><h3>鋼板</h3><p>厚板、薄板をご希望の寸法に切断します。</p></div></div>
<div class="abs slider-btn" style="left:1004px"><svg width="16" height="10" viewBox="0 0 16 10"><path d="M16 5H2M6 1L2 5l4 4" stroke="#333" fill="none"/></svg></div>
<div class="abs slider-btn" style="left:1080px"><svg width="16" height="10" viewBox="0 0 16 10"><path d="M0 5h14M10 1l4 4-4 4" stroke="#333" fill="none"/></svg></div>

<div class="photo recruit-photo" role="img" aria-label="工場で働くスタッフの写真"></div>
<section class="abs recruit-panel">
  <span class="label">Recruit</span>
  <h2>材料という<br>製造業の根幹を<br>担う仕事</h2>
  <p>私たちが扱う鋼材は、あらゆるものづくりの出発点です。地域の製造業を支えるやりがいのある仕事に、一緒に挑戦してみませんか。</p>
  <div class="btn-line">採用情報</div>
</section>

<section class="abs info">
  <span class="label">Information</span>
  <h2>お知らせ</h2>
  <p>2024.04.01　ホームページをリニューアルいたしました。今後ともよろしくお願いいたします。</p>
</section>

<footer class="abs site-footer">
  <p class="footer-note">ご質問やご相談はお気軽にどうぞ</p>
  <div class="footer-contact" style="left:0">
    <div class="big"><svg width="34" height="34" viewBox="0 0 24 24"><path d="M6.6 10.8a15 15 0 006.6 6.6l2.2-2.2a1 1 0 011-.25 11.4 11.4 0 003.6.57 1 1 0 011 1V20a1 1 0 01-1 1A17 17 0 013 4a1 1 0 011-1h3.5a1 1 0 011 1 11.4 11.4 0 00.57 3.6 1 1 0 01-.25 1z" fill="#fff"/></svg>0256-41-7730</div>
    <small>受付時間 8:00〜17:00(土日祝除く)</small>
  </div>
  <div class="footer-divider"></div>
  <div class="footer-contact" style="left:600px">
    <div class="big" style="font-family:'Noto Sans JP',sans-serif;font-size:34px"><svg width="34" height="26" viewBox="0 0 26 20"><rect x="1" y="1" width="24" height="18" fill="none" stroke="#fff" stroke-width="2"/><path d="M1 1l12 10 12-10" fill="none" stroke="#fff" stroke-width="2"/></svg>お問い合わせ</div>
    <small>メールフォームでのお問い合わせ</small>
  </div>
  <div class="brand"><span class="mark"></span>越前カナメ鋼業株式会社</div>
  <nav class="footer-nav"><span>事業内容</span><span>会社概要</span><span>採用情報</span><span>お問い合わせ</span></nav>
  <p class="footer-address">〒959-0200 新潟県燕市大町二丁目4-12　TEL 0256-41-7730 / FAX 0256-41-7731</p>
  <div class="footer-bottom"><span>プライバシーポリシー</span><span>サイトマップ</span><span class="en">© 2024 Echizen Kaname Kogyo Co., Ltd. All Rights Reserved.</span></div>
  <div class="to-top"><svg width="12" height="16" viewBox="0 0 12 16"><path d="M6 16V2M1 7l5-5 5 5" stroke="#fff" fill="none"/></svg></div>
</footer>

</body>
</html>
```